Lumorax Helpdesk overview brochure

Take the word document that is attached and turn it into a brochure. (Thinking one page, front and back.) the only existing branding/colors we have is the logo that is on the document. It may require a phone all or a bit of back and forth in text to explain some of the concepts in the attached document.

Target Market(s)

Call centers

Industry/Entity Type

It Service

Font styles to use
Sans Serif

Colors

Designer to choose colors to be used in the design.

Requirements
Must have
• A crisp professional look

```html
<!DOCTYPE html>
<html lang="en">
<head>
<meta charset="utf-8">
<title>Lumorax Helpdesk – Overview Brochure</title>
<link rel="stylesheet" href="https://fonts.googleapis.com/css2?family=Open+Sans:ital,wght@0,400;0,600;0,700;1,700&display=swap">
<style>
  :root {
    --steel-blue: #5a8fb2;
    --accent-blue: #2aa7e0;
    --paper: #ffffff;
    --paper-shade: #f1f4f6;
    --ink: #4a4d52;
    --ink-soft: #5d6166;
    --backdrop: #e9ebed;
    --photo-glow: #e6eff5;
    --photo-light: #b9d0de;
    --photo-mid: #7fa3bb;
    --photo-dark: #4a7490;
  }
  * { box-sizing: border-box; margin: 0; padding: 0; }
  html, body { width: 1200px; height: 857px; overflow: hidden; }
  body {
    background: var(--backdrop);
    font-family: "Open Sans", Arial, sans-serif;
    display: flex;
    align-items: center;
    justify-content: center;
  }
  .brochure-spread {
    display: flex;
    width: 1040px;
    height: 735px;
    box-shadow: 0 6px 24px rgba(0,0,0,0.12);
  }
  .panel {
    width: 520px;
    height: 100%;
    display: flex;
    flex-direction: column;
    background: var(--paper);
  }
  .accent-band { height: 10px; background: var(--accent-blue); flex: none; }
  .panel-foot {
    flex: 1;
    display: flex;
    flex-direction: column;
    align-items: center;
    justify-content: center;
    background: linear-gradient(180deg, var(--paper) 0%, var(--paper-shade) 100%);
    border-bottom: 10px solid var(--accent-blue);
  }

  /* Back panel */
  .contact-block {
    height: 500px;
    background: var(--steel-blue);
    display: flex;
    flex-direction: column;
    align-items: center;
    justify-content: center;
    gap: 28px;
    color: var(--paper);
  }
  .contact-item { display: flex; flex-direction: column; align-items: center; gap: 12px; }
  .contact-icon { width: 44px; height: 44px; }
  .contact-text { font-size: 15px; letter-spacing: 0.8px; }

  .brand-lockup { display: flex; align-items: center; gap: 16px; }
  .brand-dot {
    width: 54px; height: 54px; border-radius: 50%;
    background: var(--accent-blue); flex: none;
  }
  .brand-name {
    font-size: 34px; font-weight: 600; color: var(--ink);
    line-height: 1.05; letter-spacing: 1px;
  }
  .tagline {
    margin-top: 36px;
    font-size: 15px; font-weight: 600; letter-spacing: 2.6px;
    color: var(--ink-soft); text-transform: uppercase;
  }
  .tagline em { color: var(--accent-blue); font-style: italic; font-weight: 700; }

  /* Front panel */
  .cover-hero {
    height: 420px;
    position: relative;
    background:
      radial-gradient(ellipse 38% 48% at 40% 58%, rgba(230,239,245,0.95) 0%, rgba(230,239,245,0) 100%),
      radial-gradient(ellipse 34% 30% at 72% 40%, rgba(214,230,240,0.75) 0%, rgba(214,230,240,0) 100%),
      radial-gradient(ellipse 70% 80% at 50% 55%, var(--photo-light) 0%, var(--photo-mid) 60%, var(--photo-dark) 100%);
  }
  .cover-headline {
    position: absolute; top: 24px; left: 50%;
    width: 380px; transform: translateX(-50%);
    text-align: center; color: var(--paper);
    font-size: 14px; font-weight: 700; line-height: 1.5; letter-spacing: 0.9px;
  }
  .cover-foot { gap: 30px; }
  .cover-foot .brand-name { font-size: 38px; }
  .cover-web {
    align-self: flex-end; margin-right: 44px;
    font-size: 15px; font-weight: 600; color: var(--ink-soft); letter-spacing: 0.8px;
  }
</style>
</head>
<body>
  <main class="brochure-spread">
    <section class="panel panel-back">
      <div class="contact-block">
        <div class="contact-item">
          <svg class="contact-icon" viewBox="0 0 46 46" aria-hidden="true">
            <circle cx="23" cy="23" r="21" fill="none" stroke="#fff" stroke-width="2.5"/>
            <path d="M13 20c0-4 20-4 20 0v2h-5v-2c-3-1-7-1-10 0v2h-5z" fill="#fff"/>
            <rect x="16" y="23" width="14" height="9" rx="2" fill="#fff"/>
            <circle cx="23" cy="27.5" r="2.5" fill="var(--steel-blue)"/>
          </svg>
          <span class="contact-text">555-014-2290</span>
        </div>
        <div class="contact-item">
          <svg class="contact-icon" viewBox="0 0 46 46" aria-hidden="true">
            <circle cx="23" cy="23" r="21" fill="none" stroke="#fff" stroke-width="2.5"/>
            <rect x="12" y="15" width="22" height="16" rx="1.5" fill="#fff"/>
            <path d="M12 16l11 9 11-9" fill="none" stroke="var(--steel-blue)" stroke-width="2"/>
          </svg>
          <span class="contact-text">sales@lumoraxhelpdesk.net</span>
        </div>
        <div class="contact-item">
          <svg class="contact-icon" viewBox="0 0 46 46" aria-hidden="true">
            <circle cx="23" cy="23" r="21" fill="none" stroke="#fff" stroke-width="2.5"/>
            <circle cx="23" cy="23" r="11" fill="#fff"/>
            <path d="M12 23h22M23 12c-5 6-5 16 0 22M23 12c5 6 5 16 0 22" fill="none" stroke="var(--steel-blue)" stroke-width="1.6"/>
          </svg>
          <span class="contact-text">www.LumoraxHelpdesk.net</span>
        </div>
      </div>
      <div class="accent-band"></div>
      <div class="panel-foot">
        <div class="brand-lockup">
          <span class="brand-dot"></span>
          <span class="brand-name">Lumorax<br>Helpdesk</span>
        </div>
        <p class="tagline">The next leap <em>forward</em> in customer service</p>
      </div>
    </section>

    <section class="panel panel-front">
      <div class="cover-hero" role="img" aria-label="Photo of a smiling contact-center agent wearing a headset, arms folded, in front of a glowing digital world map">
        <p class="cover-headline">HELPING CONTACT CENTERS Serve New Customer Access Channels, Improve Customer Service, and Lower Costs of Operation</p>
      </div>
      <div class="accent-band"></div>
      <div class="panel-foot cover-foot">
        <div class="brand-lockup">
          <span class="brand-dot"></span>
          <span class="brand-name">Lumorax<br>Helpdesk</span>
        </div>
        <span class="cover-web">www.LumoraxHelpdesk.net</span>
      </div>
    </section>
  </main>
</body>
</html>
```